GridMonarch : This is a Puzzle and This is not a Puzzle

GridMonarch is a new addictive way to play Sudoku (see description on the attached document).
We would like your help in developing a design for the playscreen of the game (a mock-up is in the attached document)
The winner will be entrusted with the work of the complete design of the application (home screen, configuration screen, etc.) in a specific contract.
Thank you from Paris France.
Best.
Bertrand

```html
<!DOCTYPE html>
<html lang="en">
<head>
<meta charset="utf-8">
<title>GridMonarch – Play Screen</title>
<link rel="stylesheet" href="https://fonts.googleapis.com/css2?family=Poppins:wght@500;600&display=swap">
<style>
  :root {
    --stage: #0d0d0d;
    --panel: #0a6ad2;
    --button: #2a88e4;
    --badge: #2f8fe8;
    --board: #ffffff;
    --icon: #ffffff;
    --accent: #ffee00;
    --star-soft: #a9d3ff;
    --star-red: #ff1a1a;
    --c-red: #ff0000;
    --c-magenta: #ff00ff;
    --c-yellow: #ffff00;
    --c-gray: #c0c0c4;
    --c-black: #000000;
    --c-navy: #0000c4;
    --c-gold: #c8960c;
    --c-green: #00f000;
    --c-cyan: #00ffff;
    --digit-light: #ffffff;
    --digit-dark: #1060c8;
  }
  * { box-sizing: border-box; margin: 0; padding: 0; }
  html, body {
    width: 1200px; height: 1200px; overflow: hidden;
    background: var(--stage);
    font-family: "Poppins", sans-serif;
  }
  .play-screen {
    position: absolute; left: 51px; top: 347px;
    width: 844px; height: 390px;
    transform: scale(1.3); transform-origin: 0 0;
    background: var(--panel); border-radius: 22px;
  }
  .rating {
    position: absolute; top: 13px; width: 20px; height: 103px;
    border-radius: 3px; display: flex; flex-direction: column;
    align-items: center; padding-top: 2px; gap: 0;
  }
  .rating--player { left: 54px; background: var(--board); }
  .rating--level { left: 82px; background: var(--button); }
  .rating svg { width: 15px; height: 15px; display: block; margin-top: 1.5px; }
  .tool {
    position: absolute; width: 48px; height: 48px; border-radius: 6px;
    background: var(--button); display: flex; align-items: center; justify-content: center;
  }
  .tool svg { width: 30px; height: 30px; }
  .tool--left { left: 54px; }
  .tool--right { left: 742px; }
  .board {
    position: absolute; left: 126px; top: 0; width: 592px; height: 390px;
    background: var(--board); border-radius: 14px;
  }
  .column {
    position: absolute; top: 13px; display: grid; row-gap: 4px;
    grid-auto-rows: 36px;
  }
  .column > :nth-child(4), .column > :nth-child(7) { margin-top: 4px; }
  .badge {
    align-self: center; width: 24px; height: 24px; border-radius: 3px;
    background: var(--badge); color: var(--digit-light);
    font-size: 13px; font-weight: 500; display: flex; align-items: center; justify-content: center;
  }
  .column--counts-left { left: 20px; }
  .column--swatches { left: 48px; }
  .column--numbers { left: 508px; }
  .column--counts-right { left: 548px; }
  .swatch { width: 36px; height: 36px; border-radius: 2px; }
  .number-key {
    width: 36px; height: 36px; border-radius: 3px; background: var(--panel);
    color: var(--digit-light); font-size: 18px; font-weight: 500;
    display: flex; align-items: center; justify-content: center;
  }
  .grid {
    position: absolute; left: 114px; top: 13px;
    display: grid; grid-template-columns: repeat(9, 36px); grid-auto-rows: 36px; gap: 4px;
  }
  .cell {
    border-radius: 3px; color: var(--digit-light);
    font-size: 18px; font-weight: 600; display: flex; align-items: center; justify-content: center;
  }
  .cell:nth-child(9n+4), .cell:nth-child(9n+7) { margin-left: 4px; }
  .cell:nth-child(n+28):nth-child(-n+36), .cell:nth-child(n+55):nth-child(-n+63) { margin-top: 4px; }
  .red { background: var(--c-red); }
  .magenta { background: var(--c-magenta); }
  .yellow { background: var(--c-yellow); color: var(--digit-dark); }
  .gray { background: var(--c-gray); }
  .black { background: var(--c-black); }
  .navy { background: var(--c-navy); }
  .gold { background: var(--c-gold); }
  .green { background: var(--c-green); }
  .cyan { background: var(--c-cyan); color: var(--digit-dark); }
</style>
</head>
<body>
<svg width="0" height="0" style="position:absolute">
  <defs>
    <path id="star" d="M12 2l2.9 6.6 7.1.6-5.4 4.7 1.6 7L12 17.2 5.8 20.9l1.6-7L2 9.2l7.1-.6z"/>
  </defs>
</svg>

<main class="play-screen">
  <div class="rating rating--player" aria-label="Player rating">
    <svg viewBox="0 0 24 24"><use href="#star" fill="var(--star-soft)"/></svg>
    <svg viewBox="0 0 24 24"><use href="#star" fill="var(--star-soft)"/></svg>
    <svg viewBox="0 0 24 24"><use href="#star" fill="var(--star-soft)"/></svg>
    <svg viewBox="0 0 24 24"><use href="#star" fill="var(--star-red)"/></svg>
    <svg viewBox="0 0 24 24"><use href="#star" fill="var(--star-red)"/></svg>
    <svg viewBox="0 0 24 24"><circle cx="12" cy="12" r="11" fill="var(--panel)"/><use href="#star" fill="#fff" transform="translate(4 4) scale(.66)"/></svg>
  </div>
  <div class="rating rating--level" aria-label="Level rating">
    <svg viewBox="0 0 24 24"><use href="#star" fill="var(--star-soft)"/></svg>
    <svg viewBox="0 0 24 24"><use href="#star" fill="var(--star-soft)"/></svg>
    <svg viewBox="0 0 24 24"><use href="#star" fill="var(--star-soft)"/></svg>
    <svg viewBox="0 0 24 24"><use href="#star" fill="var(--star-soft)"/></svg>
    <svg viewBox="0 0 24 24"><use href="#star" fill="var(--accent)"/></svg>
    <svg viewBox="0 0 24 24"><circle cx="12" cy="12" r="11" fill="#fff"/><use href="#star" fill="var(--button)" transform="translate(4 4) scale(.66)"/></svg>
  </div>

  <div class="tool tool--left" style="top:161px" aria-label="Undo">
    <svg viewBox="0 0 30 30"><path d="M14 8v14L4 15zM26 8v14L16 15z" fill="var(--icon)"/></svg>
  </div>
  <div class="tool tool--left" style="top:217px" aria-label="Show grid">
    <svg viewBox="0 0 30 30" fill="none" stroke="var(--accent)" stroke-width="2.4"><rect x="4" y="6" width="8" height="8"/><rect x="4" y="18" width="8" height="8"/><rect x="16" y="18" width="8" height="8"/><path d="M15 9.5q6-6 12 0q-6 6-12 0z"/><circle cx="21" cy="9.5" r="1.6" fill="var(--accent)"/></svg>
  </div>
  <div class="tool tool--left" style="top:273px" aria-label="Erase">
    <svg viewBox="0 0 30 30"><path d="M16 4l10 10-8 8H10l-6-6z" fill="var(--icon)"/><path d="M9 11l10 10" stroke="var(--button)" stroke-width="2"/><rect x="4" y="24" width="22" height="2.4" fill="var(--icon)"/></svg>
  </div>
  <div class="tool tool--left" style="top:329px" aria-label="Hint">
    <svg viewBox="0 0 30 30"><path d="M15 3a8 8 0 0 0-5 14.2V21h10v-3.8A8 8 0 0 0 15 3z" fill="var(--accent)"/><rect x="10.5" y="22.5" width="9" height="2.2" rx="1" fill="var(--accent)"/><rect x="12" y="26" width="6" height="2" rx="1" fill="var(--accent)"/></svg>
  </div>

  <div class="tool tool--right" style="top:13px" aria-label="Home">
    <svg viewBox="0 0 30 30"><path d="M15 4L3 15h4v11h6v-7h4v7h6V15h4z" fill="var(--icon)"/></svg>
  </div>
  <div class="tool tool--right" style="top:69px" aria-label="Timer 60">
    <svg viewBox="0 0 30 30"><path d="M8 8.5A10.5 10.5 0 1 1 5.2 17" fill="none" stroke="var(--icon)" stroke-width="2.2"/><path d="M4 5l6 1-3 5z" fill="var(--icon)"/><text x="15.5" y="19.5" text-anchor="middle" font-family="Poppins, sans-serif" font-weight="600" font-size="9.5" fill="var(--icon)">60</text></svg>
  </div>
  <div class="tool tool--right" style="top:161px" aria-label="Redo">
    <svg viewBox="0 0 30 30"><path d="M4 8v14l10-7zM16 8v14l10-7z" fill="var(--icon)"/></svg>
  </div>
  <div class="tool tool--right" style="top:217px" aria-label="Show grid">
    <svg viewBox="0 0 30 30" fill="none" stroke="var(--icon)" stroke-width="2.4"><rect x="4" y="6" width="8" height="8"/><rect x="4" y="18" width="8" height="8"/><rect x="16" y="18" width="8" height="8"/><path d="M15 9.5q6-6 12 0q-6 6-12 0z"/><circle cx="21" cy="9.5" r="1.6" fill="var(--icon)"/></svg>
  </div>
  <div class="tool tool--right" style="top:273px" aria-label="Erase">
    <svg viewBox="0 0 30 30"><path d="M16 4l10 10-8 8H10l-6-6z" fill="var(--icon)"/><path d="M9 11l10 10" stroke="var(--button)" stroke-width="2"/><rect x="4" y="24" width="22" height="2.4" fill="var(--icon)"/></svg>
  </div>
  <div class="tool tool--right" style="top:329px" aria-label="Hint">
    <svg viewBox="0 0 30 30" fill="none" stroke="var(--icon)" stroke-width="2"><path d="M15 4a7.5 7.5 0 0 0-4.5 13.5V21h9v-3.5A7.5 7.5 0 0 0 15 4z"/><path d="M11 24h8M12.5 27h5"/></svg>
  </div>

  <section class="board">
    <div class="column column--counts-left">
      <span class="badge">1</span><span class="badge">4</span><span class="badge">4</span>
      <span class="badge">2</span><span class="badge">6</span><span class="badge">5</span>
      <span class="badge">7</span><span class="badge">5</span><span class="badge">2</span>
    </div>
    <div class="column column--swatches">
      <span class="swatch red"></span><span class="swatch magenta"></span><span class="swatch yellow"></span>
      <span class="swatch gray"></span><span class="swatch black"></span><span class="swatch navy"></span>
      <span class="swatch gold"></span><span class="swatch green"></span><span class="swatch cyan"></span>
    </div>

    <div class="grid">
      <span class="cell navy">1</span><span class="cell cyan">8</span><span class="cell gold">2</span><span class="cell red">1</span><span class="cell gray">8</span><span class="cell black">2</span><span class="cell magenta">1</span><span class="cell yellow">8</span><span class="cell green">2</span>
      <span class="cell gray">3</span><span class="cell black">5</span><span class="cell magenta">9</span><span class="cell cyan">3</span><span class="cell green">5</span><span class="cell yellow">9</span><span class="cell red">3</span><span class="cell navy">5</span><span class="cell gold">9</span>
      <span class="cell red">6</span><span class="cell green">7</span><span class="cell yellow">4</span><span class="cell magenta">6</span><span class="cell gold">7</span><span class="cell navy">4</span><span class="cell cyan">6</span><span class="cell gray">7</span><span class="cell black">4</span>
      <span class="cell cyan">1</span><span class="cell red">8</span><span class="cell navy">2</span><span class="cell gold">1</span><span class="cell black">8</span><span class="cell magenta">2</span><span class="cell yellow">1</span><span class="cell green">8</span><span class="cell gray">2</span>
      <span class="cell magenta">3</span><span class="cell gray">5</span><span class="cell black">9</span><span class="cell yellow">3</span><span class="cell red">5</span><span class="cell green">9</span><span class="cell navy">3</span><span class="cell gold">5</span><span class="cell cyan">9</span>
      <span class="cell yellow">6</span><span class="cell gold">7</span><span class="cell green">4</span><span class="cell gray">6</span><span class="cell navy">7</span><span class="cell cyan">4</span><span class="cell black">6</span><span class="cell magenta">7</span><span class="cell red">4</span>
      <span class="cell black">1</span><span class="cell navy">8</span><span class="cell gray">2</span><span class="cell green">1</span><span class="cell yellow">8</span><span class="cell red">2</span><span class="cell gold">1</span><span class="cell cyan">8</span><span class="cell magenta">2</span>
      <span class="cell gold">3</span><span class="cell yellow">5</span><span class="cell cyan">9</span><span class="cell black">3</span><span class="cell magenta">5</span><span class="cell gray">9</span><span class="cell green">3</span><span class="cell red">5</span><span class="cell navy">9</span>
      <span class="cell green">6</span><span class="cell magenta">7</span><span class="cell red">4</span><span class="cell navy">6</span><span class="cell cyan">7</span><span class="cell gold">4</span><span class="cell gray">6</span><span class="cell black">7</span><span class="cell yellow">4</span>
    </div>

    <div class="column column--numbers">
      <span class="number-key">1</span><span class="number-key">2</span><span class="number-key">3</span>
      <span class="number-key">4</span><span class="number-key">5</span><span class="number-key">6</span>
      <span class="number-key">7</span><span class="number-key">8</span><span class="number-key">9</span>
    </div>
    <div class="column column--counts-right">
      <span class="badge">1</span><span class="badge">4</span><span class="badge">4</span>
      <span class="badge">2</span><span class="badge">6</span><span class="badge">5</span>
      <span class="badge">7</span><span class="badge">5</span><span class="badge">2</span>
    </div>
  </section>
</main>
</body>
</html>
```